Bright Harbor Family Law Firm Website Renovation

We need a website redesign in SquareSpace that is more modern, user friendly, on brand, less cluttered, easier to navigate, conveys clearly what our services are, and has clear, visible calls to action.

We would like to hire and work with the winning designer to complete the remaining pages of the site.
Updates

Gathering more feedback

Target Market(s)

Couples looking for divorce representation or mediation who have a conscious, progressive mindset. They are self-aware and personal development plays an important role in their lives. They want an amicable interaction and aspire to have a healthy relationship after divorce.

Age range: 30-60
Income 100K+ household

Industry/Entity Type

Family Law

Font styles to use
Sans Serif

Colors
85acd3
33a6d7
50c0af
a0cd3a

Requirements
Must have
• Please see attached doc for full creative brief details.

"Changing the way people divorce" on top of site.
Images that show happy clients and that represent males and females. Diversity inclusion is also be important.
We are looking for warm, welcoming design and imagery.
Should not have
• Not heavily attorney focused.
Please see attached brief for full description.

```html
<!DOCTYPE html>
<html lang="en">
<head>
<meta charset="utf-8">
<title>Bright Harbor Family Law</title>
<link href="https://fonts.googleapis.com/css2?family=Bree+Serif&family=Quicksand:wght@300;400;500;600&family=Open+Sans:wght@400;600;700&family=Courier+Prime&display=swap" rel="stylesheet">
<style>
:root{
  --sky:#85acd3;
  --blue:#33a6d7;
  --teal:#50c0af;
  --orange:#f07b2f;
  --ink:#3a3a3a;
  --muted:#6b6b6b;
  --frame:#e4e4e4;
  --screen:#1d1d1f;
  --white:#ffffff;
  --red:#c8102e;
  --footer:#86add8;
  --badge:#e6ebf0;
}
*{margin:0;padding:0;box-sizing:border-box}
html,body{width:1200px;height:3242px;overflow:hidden;background:var(--white)}
body{position:relative;font-family:'Quicksand',sans-serif;color:var(--ink)}
.abs{position:absolute}

/* hero */
.hero{left:0;top:0;width:1200px;height:606px;background:linear-gradient(180deg,#6f9cc9 0%,#86acd3 55%,#a9c3df 100%)}
.brand{left:150px;top:96px;width:140px;text-align:center}
.brand-name{font-family:'Quicksand',sans-serif;font-weight:500;font-size:13px;letter-spacing:2px;color:#2f3b4a;line-height:16px}
.call{right:150px;top:30px;text-align:right;color:var(--white)}
.call small{display:block;font-family:'Open Sans',sans-serif;font-size:12px}
.call strong{font-family:'Quicksand',sans-serif;font-weight:400;font-size:22px}
.nav{right:150px;top:90px;display:flex;gap:10px;align-items:center;font-family:'Open Sans',sans-serif;font-size:12.5px;color:var(--white)}
.nav .dot{opacity:.8}
.nav .active{font-weight:700}
.nav .boxed{border:1px solid var(--white);border-radius:3px;padding:4px 4px}
.hero-title{left:0;width:1200px;top:236px;text-align:center;font-family:'Bree Serif',serif;font-size:56px;letter-spacing:6px;color:var(--white);text-shadow:0 2px 4px rgba(0,0,0,.25)}
.hero-sub{left:0;width:1200px;top:316px;text-align:center;font-family:'Quicksand',sans-serif;font-weight:500;font-size:21px;letter-spacing:4px;color:var(--white)}
.btn{display:inline-block;background:var(--blue);color:var(--white);font-family:'Open Sans',sans-serif;font-weight:700;font-size:12px;text-align:center;text-transform:uppercase}
.hero-btn{left:487px;top:402px;width:226px;height:37px;line-height:37px}

/* tablets */
.tablet{background:var(--frame);border-radius:16px}
.tablet .screen{position:absolute;background:var(--screen)}
.tablet .cam{position:absolute;width:20px;height:20px;border-radius:50%;background:#d2d2d2}
.tablet .side{position:absolute;width:10px;height:70px;border-radius:5px;background:#d2d2d2}
.shadow{height:14px;border-radius:50%;background:radial-gradient(ellipse at center,rgba(0,0,0,.28) 0%,rgba(0,0,0,0) 70%)}
.play{position:absolute;width:48px;height:48px;border-radius:50%;background:var(--blue)}
.play::after{content:"";position:absolute;left:19px;top:13px;border-left:16px solid var(--white);border-top:11px solid transparent;border-bottom:11px solid transparent}

.h-section{font-family:'Quicksand',sans-serif;font-weight:400;font-size:30px;letter-spacing:1.5px;color:var(--ink)}
.p-body{font-family:'Quicksand',sans-serif;font-size:13px;line-height:23px;color:var(--muted);letter-spacing:.6px}

/* services band */
.services{left:0;top:1047px;width:1200px;height:372px;background:linear-gradient(90deg,#7fa4d0 0%,#ffffff 20%,#ffffff 80%,#7fa4d0 100%)}
.svc-divider{left:599px;top:1110px;width:1px;height:180px;background:#d9e6f1}
.svc-title{width:420px;text-align:center}
.svc-text{width:382px;text-align:justify;font-size:11.5px;line-height:22.5px}
.svc-text b{color:var(--ink);font-weight:600}
.svc-btn{width:225px;height:37px;line-height:37px}

/* questionnaire */
.quiz{left:0;top:1463px;width:1200px;height:169px;background:var(--teal)}
.quiz h2{position:absolute;left:183px;top:30px;font-family:'Open Sans',sans-serif;font-weight:700;font-size:27px;color:var(--white)}
.quiz p{position:absolute;left:184px;top:77px;width:385px;font-size:13px;line-height:16px;color:var(--white);letter-spacing:.5px}
.quiz .btn{position:absolute;left:671px;top:67px;width:267px;height:37px;line-height:37px;background:var(--orange);font-size:14.5px;font-weight:600}

/* reviews */
.reviews{left:150px;top:2043px;width:900px;height:399px;border:1px solid var(--blue)}
.reviews h2{text-align:center;margin-top:28px}
.quote{position:absolute;left:103px;top:112px;width:694px;text-align:center;font-family:'Courier Prime',monospace;font-size:14.5px;line-height:22.5px;color:var(--muted)}
.stars{position:absolute;left:0;width:100%;top:245px;text-align:center;color:var(--red);font-size:20px;letter-spacing:3px}
.reviewer{position:absolute;left:0;width:100%;top:285px;text-align:center;font-family:'Courier Prime',monospace;font-style:italic;font-size:12px;color:var(--muted);letter-spacing:1px}
.reviews .btn{position:absolute;left:338px;top:328px;width:225px;height:37px;line-height:37px}
.arrow{position:absolute;top:188px}

/* rated */
.rated-band{left:0;top:2570px;width:1200px;height:260px;background:var(--blue)}
.rated-label{left:185px;top:2678px;font-size:29px;color:var(--white);letter-spacing:1px}
.tile{width:224px;height:164px;background:var(--white);border:1px solid var(--blue);display:flex;align-items:center;justify-content:center}
.badge{width:150px;height:110px;border-radius:6px;background:var(--badge)}
.browse{left:852px;top:2689px;width:150px;height:24px;border:1px solid var(--white);color:var(--white);font-family:'Open Sans',sans-serif;font-weight:700;font-size:11px;display:flex;align-items:center;justify-content:center;gap:10px}

/* social + footer */
.social{left:0;top:2913px;width:1200px;height:36px;background:var(--blue);font-family:'Open Sans',sans-serif;font-size:11px;color:var(--white)}
.social .item{position:absolute;top:9px;display:flex;align-items:center;gap:8px}
.social .ic{width:20px;height:20px;border-radius:50%;background:var(--white)}
.footer{left:0;top:2949px;width:1200px;height:293px;background:var(--footer);color:var(--white)}
.footer .small{font-size:10.5px;line-height:18px;letter-spacing:.4px}
.search{left:729px;top:2989px;width:322px;height:36px;background:var(--white);border:1px solid var(--blue)}
.search span{position:absolute;left:8px;top:11px;font-size:9px;color:#b5b5b5}
.search .go{position:absolute;right:0;top:0;width:36px;height:34px;background:var(--blue)}
</style>
</head>
<body>

<header>
  <div class="abs hero" role="img" aria-label="Photo of a smiling family with a toddler and a young child outdoors on a snowy plain, tinted blue"></div>
  <div class="abs brand">
    <div class="brand-name">BRIGHT HARBOR<br>FAMILY LAW</div>
  </div>
  <div class="abs call"><small>Call For A Free Consultation</small><strong>(415) 555-0147</strong></div>
  <nav class="abs nav">
    <span class="active">Home</span><span class="dot">·</span>
    <span class="boxed">Our Services</span><span class="dot">·</span>
    <span>Testimonials</span><span class="dot">·</span>
    <span>Schedule / Contact</span><span class="dot">·</span>
    <span>About Us</span><span class="dot">·</span>
    <span>FAQ</span><span class="dot">·</span>
    <span>Resources</span>
  </nav>
  <h1 class="abs hero-title">Bright Harbor</h1>
  <p class="abs hero-sub">Changing the Way People Divorce.</p>
  <a class="abs btn hero-btn">Request a free consultation</a>
</header>

<section>
  <div class="abs tablet" style="left:150px;top:659px;width:430px;height:300px">
    <div class="side" style="left:12px;top:115px"></div>
    <div class="cam" style="left:400px;top:140px"></div>
    <div class="screen" style="left:36px;top:16px;width:356px;height:270px">
      <div class="abs" role="img" aria-label="Video still of the firm introduction with the caption Learn how we are changing the way people divorce" style="left:0;top:0;width:356px;height:240px;background:linear-gradient(180deg,#2b2b2d 0%,#2b2b2d 62%,#4d6e8c 62%,#5b7896 100%)"></div>
      <div class="play" style="left:155px;top:110px"></div>
      <div class="abs" style="left:0;top:238px;width:356px;height:3px;background:#e0e0e0"></div>
      <div class="abs" style="left:0;top:238px;width:115px;height:3px;background:var(--blue)"></div>
      <svg class="abs" style="left:12px;top:248px" width="334" height="18" viewBox="0 0 334 18">
        <g fill="#33a6d7"><rect x="0" y="2" width="2" height="14"/><path d="M14 2 L4 9 L14 16Z"/><path d="M30 2 L42 9 L30 16Z"/><path d="M58 2 L68 9 L58 16Z"/><rect x="68" y="2" width="2" height="14"/>
        <circle cx="284" cy="9" r="6"/></g>
        <g fill="none" stroke="#33a6d7" stroke-width="2"><rect x="298" y="4" width="16" height="10"/><path d="M322 6V2h4M330 2h4v4M334 12v4h-4M326 16h-4v-4"/></g>
      </svg>
    </div>
  </div>
  <div class="abs shadow" style="left:150px;top:975px;width:436px"></div>
  <h2 class="abs h-section" style="left:663px;top:740px">Who we are</h2>
  <p class="abs p-body" style="left:664px;top:792px;width:384px">Our simple, free questionnaire can help you determine if you and your spouse are suited for mediation, or if you may want legal representation for yourself.</p>
</section>

<section>
  <div class="abs services"></div>
  <div class="abs svc-divider"></div>
  <h2 class="abs h-section svc-title" style="left:166px;top:1085px">Work Together</h2>
  <p class="abs p-body svc-text" style="left:185px;top:1150px">Mediation is possible when both spouses are willing to negotiate their divorce agreements in good faith, with the help of a neutral mediator. Bright Harbor attorney-mediators are experienced family lawyers and are skilled at helping clients <b>reach fair, workable agreements, without the cost and damage</b> of the conventional divorce process.</p>
  <a class="abs btn svc-btn" style="left:264px;top:1336px">Learn more</a>
  <h2 class="abs h-section svc-title" style="left:615px;top:1085px">Help Just For You</h2>
  <p class="abs p-body svc-text" style="left:634px;top:1150px">If mediation is not possible, you need a lawyer to advise, negotiate, and possibly advocate for you. Our experienced Bright Harbor lawyers offer <b>clear, confident, and highly effective advice and representation</b> while attempting to minimize financial and emotional costs to you and your family.</p>
  <a class="abs btn svc-btn" style="left:713px;top:1336px">Learn more</a>
</section>

<section class="abs quiz">
  <h2>Mediation or Lawyer?</h2>
  <p>Our simple, free questionnaire can help you determine if you and your spouse are suited for mediation, or if you may want legal representation for yourself.</p>
  <a class="btn">Take our free questionnaire</a>
</section>

<section>
  <h2 class="abs h-section" style="left:150px;top:1748px;width:420px;line-height:38px">Avoiding harm to children in divorce</h2>
  <p class="abs p-body" style="left:150px;top:1848px;width:385px">Lorem ipsum dolor sit amet, consectetur adipisicing elit, sed do eiusmod tempor incididunt ut labore et dolore magna aliqua.</p>
  <div class="abs tablet" style="left:620px;top:1677px;width:430px;height:300px">
    <div class="side" style="left:12px;top:115px"></div>
    <div class="cam" style="left:400px;top:140px"></div>
    <div class="screen" style="left:36px;top:16px;width:356px;height:270px">
      <div class="abs" role="img" aria-label="Video still of an attorney in a dark suit against a grey backdrop" style="left:58px;top:12px;width:240px;height:226px;background:linear-gradient(180deg,#5a5a5e 0%,#3e3e42 100%)"></div>
      <div class="play" style="left:155px;top:108px"></div>
      <div class="abs" style="left:0;top:238px;width:356px;height:3px;background:#e0e0e0"></div>
      <div class="abs" style="left:0;top:238px;width:112px;height:3px;background:var(--blue)"></div>
      <svg class="abs" style="left:12px;top:248px" width="334" height="18" viewBox="0 0 334 18">
        <g fill="#33a6d7"><rect x="0" y="2" width="2" height="14"/><path d="M14 2 L4 9 L14 16Z"/><path d="M30 2 L42 9 L30 16Z"/><path d="M58 2 L68 9 L58 16Z"/><rect x="68" y="2" width="2" height="14"/>
        <circle cx="284" cy="9" r="6"/></g>
        <g fill="none" stroke="#33a6d7" stroke-width="2"><rect x="298" y="4" width="16" height="10"/><path d="M322 6V2h4M330 2h4v4M334 12v4h-4M326 16h-4v-4"/></g>
      </svg>
    </div>
  </div>
  <div class="abs shadow" style="left:618px;top:1993px;width:440px"></div>
</section>

<section class="abs reviews">
  <h2 class="h-section">Our Client Reviews</h2>
  <svg class="arrow" style="left:36px" width="16" height="28" viewBox="0 0 16 28"><path d="M14 2 L2 14 L14 26" fill="none" stroke="#3a3a3a" stroke-width="2"/></svg>
  <svg class="arrow" style="right:36px" width="16" height="28" viewBox="0 0 16 28"><path d="M2 2 L14 14 L2 26" fill="none" stroke="#3a3a3a" stroke-width="2"/></svg>
  <p class="quote">“I am so grateful for my experience with Bright Harbor Family Law &amp; Mediation. I learned so much about myself and my capacity to love, grieve, and heal. You were so great at facilitating our difficult conversations, helping both of us feel validated, and coaching us on how to work well with each other moving forward in our new co-parenting relationship.”</p>
  <div class="stars">★★★★★</div>
  <div class="reviewer">Divorce Mediation Client</div>
  <a class="btn">Read more testimonal</a>
</section>

<section>
  <div class="abs rated-band"></div>
  <div class="abs rated-label">Rated by</div>
  <div class="abs tile" style="left:335px;top:2532px"><div class="badge" role="img" aria-label="Rating badge"></div></div>
  <div class="abs tile" style="left:568px;top:2532px"><div class="badge" role="img" aria-label="Award badge"></div></div>
  <div class="abs tile" style="left:335px;top:2704px"><div class="badge" role="img" aria-label="Community partner badge"></div></div>
  <div class="abs tile" style="left:568px;top:2704px"><div class="badge" role="img" aria-label="Local recommendation badge"></div></div>
  <a class="abs browse">BROWSE MORE
    <svg width="16" height="10" viewBox="0 0 16 10"><path d="M0 5H15M11 1L15 5L11 9" fill="none" stroke="#fff" stroke-width="1.2"/></svg></a>
</section>

<div class="abs social">
  <span class="item" style="left:160px"><span class="ic"></span>LIKE US ON FRIENDBOOK</span>
  <span class="item" style="left:514px"><span class="ic"></span>FOLLOW US ON CHIRPER</span>
  <span class="item" style="left:877px"><span class="ic"></span>SUBSCRIBE ON VIDSTREAM</span>
</div>

<footer class="abs footer">
  <p class="abs small" style="left:150px;top:38px">Bright Harbor Family Law &amp; Mediation LLC<br>1820 Cedar Lane, Suite 2<br>Boulder, Colorado 80302</p>
  <p class="abs small" style="left:150px;top:128px">1+ (303) 555-0192<br>hello@brightharborlaw.com</p>
  <p class="abs small" style="left:150px;top:198px;font-weight:600">Press information</p>
  <p class="abs small" style="left:150px;top:236px;font-size:9.5px">Website content copyright 2014-2020 Bright Harbor Family Law &amp; Mediation LLC</p>
  <p class="abs" style="right:150px;top:96px;font-family:'Open Sans',sans-serif;font-weight:600;font-size:12.5px;letter-spacing:.5px">We are proud to serve your family.</p>
  <p class="abs small" style="right:150px;top:152px;width:340px;text-align:right;font-size:10px">Bright Harbor Family Law &amp; Mediation LLC currently serves the legal needs of Colorado residents (including same-sex and other alternative families) in Boulder County, Denver County, Broomfield County, Larimer County, Adams County, Weld County, and Jefferson County.</p>
</footer>
<div class="abs search"><span>Search site</span>
  <div class="go"><svg style="position:absolute;left:10px;top:9px" width="16" height="16" viewBox="0 0 16 16"><circle cx="6.5" cy="6.5" r="5" fill="none" stroke="#fff" stroke-width="1.5"/><path d="M10 10L15 15" stroke="#fff" stroke-width="1.5"/></svg></div>
</div>

</body>
</html>
```